E-Sport banner for team [logo already created]

Hey,

Need a 2400 x 600 banner for our esport team we are creating.
The logo is already created, what we need is to make a banner out of it.

So, the logo shouldn't stay exactly the same, you should be creative and do something special with it.

Banner should be:
Clean
Modern
Have kinda the same theme as the logo provided
Be creative

Example of banners (not the same size):
https://img.pixovault.net/v/7kQ2mRtLpWa/fullsize.jpg
https://img.pixovault.net/v/Hn_beRoWz3c/fullsize.jpg
https://img.pixovault.net/v/qtmoYKdBvRs/fullsize.jpg
https://img.pixovault.net/v/gLP8wNnHxJd/fullsize.jpg

Check here for even more inspiration:
https://artlumora.com/tags/esports_banner

```html
<!DOCTYPE html>
<html lang="en">
<head>
<meta charset="utf-8">
<title>Volta Gaming – Esport Center Banner</title>
<link rel="stylesheet" href="https://fonts.googleapis.com/css2?family=Exo+2:wght@200;300;600&display=swap">
<style>
  :root {
    --violet-deep: #2a0d86;
    --violet-mid: #5a18c4;
    --violet-bright: #7b22e0;
    --violet-dark: #3c0b8e;
    --violet-edge: #8a5ae6;
    --white: #ffffff;
    --gold: #c9a640;
    --photo-teal: #1fa7c4;
    --photo-pink: #d04aa8;
    --photo-blue: #2a5cc0;
  }
  * { margin: 0; padding: 0; box-sizing: border-box; }
  html, body { width: 1200px; height: 300px; overflow: hidden; background: var(--violet-dark); }
  .banner {
    position: relative;
    width: 1200px;
    height: 300px;
    overflow: hidden;
    font-family: "Exo 2", sans-serif;
    color: var(--white);
    background: linear-gradient(90deg, var(--violet-deep) 0%, var(--violet-mid) 48%, var(--violet-bright) 60%, var(--violet-dark) 100%);
  }
  .backdrop { position: absolute; inset: 0; }
  .brand {
    position: absolute;
    left: 48px;
    top: 30px;
    width: 280px;
    display: flex;
    flex-direction: column;
    align-items: center;
  }
  .brand__mark {
    width: 124px;
    height: 124px;
    border-radius: 50%;
    background: var(--white);
  }
  .brand__name {
    margin-top: 26px;
    font-weight: 300;
    font-size: 35px;
    letter-spacing: 1.5px;
    line-height: 1;
    white-space: nowrap;
  }
  .brand__tagline {
    margin-top: 14px;
    font-weight: 300;
    font-size: 12px;
    letter-spacing: 4.5px;
    color: var(--gold);
    white-space: nowrap;
  }
  .headline {
    position: absolute;
    left: 360px;
    top: 83px;
    width: 476px;
    text-align: center;
  }
  .headline__kicker {
    font-weight: 200;
    font-size: 34px;
    letter-spacing: 0.5px;
    line-height: 1;
    white-space: nowrap;
  }
  .headline__title {
    margin-top: 12px;
    font-weight: 600;
    font-size: 46px;
    letter-spacing: 5px;
    line-height: 1;
    white-space: nowrap;
  }
  .photo {
    position: absolute;
    left: 885px;
    top: 34px;
    width: 245px;
    height: 256px;
    border: 6px solid rgba(138, 90, 230, 0.45);
    border-radius: 4px 4px 60px 60px;
    background: linear-gradient(120deg, var(--photo-teal) 0%, var(--photo-blue) 45%, var(--photo-pink) 100%);
    opacity: 0.9;
  }
</style>
</head>
<body>
  <div class="banner">
    <svg class="backdrop" width="1200" height="300" viewBox="0 0 1200 300" aria-hidden="true">
      <defs>
        <linearGradient id="wedge" x1="0" y1="0" x2="1" y2="1">
          <stop offset="0" stop-color="#3d23c8"/>
          <stop offset="1" stop-color="#8a22e6"/>
        </linearGradient>
        <linearGradient id="streak" x1="0" y1="0" x2="1" y2="0">
          <stop offset="0" stop-color="#ffffff" stop-opacity="0"/>
          <stop offset="0.5" stop-color="#ffffff" stop-opacity="0.7"/>
          <stop offset="1" stop-color="#ffffff" stop-opacity="0"/>
        </linearGradient>
      </defs>
      <polygon points="0,0 100,0 115,18 300,170 500,300 0,300" fill="url(#wedge)" opacity="0.75"/>
      <polyline points="100,0 115,18 300,170 520,300" fill="none" stroke="var(--violet-edge)" stroke-width="4" opacity="0.6"/>
      <polygon points="250,20 640,20 600,60 300,60" fill="#1c0a70" opacity="0.35"/>
      <polygon points="420,190 780,190 750,220 440,220" fill="#1c0a70" opacity="0.3"/>
      <polygon points="600,100 780,100 740,130 580,130" fill="#a060ff" opacity="0.18"/>
      <polygon points="480,240 760,240 720,275 460,275" fill="#a060ff" opacity="0.15"/>
      <polygon points="620,0 760,0 720,30 600,30" fill="#a060ff" opacity="0.2"/>
      <rect x="380" y="66" width="200" height="1.5" fill="url(#streak)"/>
      <rect x="420" y="191" width="260" height="1.5" fill="url(#streak)"/>
      <rect x="560" y="276" width="300" height="1.5" fill="url(#streak)"/>
      <rect x="700" y="147" width="140" height="1.5" fill="url(#streak)"/>
      <circle cx="812" cy="95" r="14" fill="#c080ff" opacity="0.18"/>
      <circle cx="862" cy="48" r="4" fill="#c080ff" opacity="0.4"/>
      <circle cx="595" cy="178" r="2" fill="#ffffff" opacity="0.6"/>
    </svg>

    <div class="brand">
      <span class="brand__mark"></span>
      <div class="brand__name">VOLTA GAMING</div>
      <div class="brand__tagline">E-SPORTCENTER</div>
    </div>

    <div class="headline">
      <p class="headline__kicker">WE ARE OPEN!</p>
      <h1 class="headline__title">ESPORT CENTER</h1>
    </div>

    <div class="photo" role="img" aria-label="Photo of a smiling gamer wearing a headset at a neon-lit gaming setup"></div>
  </div>
</body>
</html>
```